MOSS:LOOP HUB Flyer

MOSS:LOOP HUB is a social enterprise that aims to promote sustainability through enabling and interacting with the community at large by prolonging the life of our preloved apparels that promote green habits such as reusing, repurposing and recreating.

The task is to create a double sided A5 flyer that targets Crafters, Sewists and Hobbyists to book and rent our Creative Spaces for their craft projects. We would also like to showcase our webstore for preloved clothing and upcycled merchandise. The design should be engaging to attract the young crowd.
Please visit our website www.mossloophub.sg and instagram (https://www.instagram.com/mossloophubsg/) for reference on what we do.

Target Market(s)

Crafters, Sewists and Hobbyists. Young crowd between 16 to 45 years old

Requirements
Must have
• fun culture to create and upcycle fabric and to our part for the society
Heavy emphasis on Creative Spaces
Nice to have
• promote MOSS:LOOP HUB as the curated platform to source, supply and
contribute towards Circular Fashion.
Should not have
• Do not reflect us as a thrift store

```html
<!DOCTYPE html>
<html lang="en">
<head>
<meta charset="utf-8">
<title>MOSS:LOOP HUB Flyer</title>
<link rel="stylesheet" href="https://fonts.googleapis.com/css2?family=Bebas+Neue&family=Montserrat:wght@400;500;600;700&display=swap">
<style>
:root{
  --green:#4ba23f;
  --green-dark:#3d8a33;
  --ink:#3a3a3a;
  --ink-soft:#555;
  --white:#ffffff;
  --stage:#dcdee2;
  --paper:#eeeff0;
  --caption:rgba(70,70,70,.78);
}
*{box-sizing:border-box;margin:0;padding:0}
html,body{width:1200px;height:800px;overflow:hidden}
body{background:var(--stage);position:relative;font-family:'Montserrat',sans-serif;color:var(--ink)}
.page{position:absolute;top:96px;width:429px;height:606px;overflow:hidden;background:linear-gradient(160deg,#f7f7f7 0%,var(--paper) 55%,#e2e3e5 100%);box-shadow:0 6px 18px rgba(0,0,0,.25)}
.page--front{left:125px}
.page--back{left:646px}

/* FRONT */
.hero-photo{position:absolute;left:0;top:0;width:429px;height:340px;
  background:linear-gradient(120deg,#c9d85a 0%,#9fb348 35%,#6f8a3a 60%,#8c6b3c 80%,#b64a3a 100%);
  clip-path:path('M0 0 H429 V272 Q300 330 215 300 Q120 265 0 290 Z')}
.hero-frame{position:absolute;left:0;top:0;width:429px;height:360px}
.brand-tab{position:absolute;left:110px;top:0;width:210px;height:80px;display:flex;align-items:center;justify-content:center}
.brand-name{font-family:'Montserrat',sans-serif;font-weight:700;font-size:12px;color:var(--white);letter-spacing:.5px;position:relative;top:-4px}
.headline{position:absolute;left:19px;top:120px;font-family:'Bebas Neue',sans-serif;color:var(--white);line-height:.98;text-shadow:0 2px 4px rgba(0,0,0,.35)}
.headline span{display:block}
.headline .l1{font-size:44px;letter-spacing:.3px}
.headline .l2{font-size:56px}
.headline .l3{font-size:44px}
.spot{position:absolute;border-radius:50%;border:4px solid var(--white);box-shadow:0 2px 6px rgba(0,0,0,.25)}
.spot--hangers{left:61px;top:308px;width:88px;height:88px;background:linear-gradient(135deg,#f4d9b8,#c9e3ee 60%,#f1c6d6)}
.spot--hoops{left:151px;top:290px;width:128px;height:128px;border:5px solid #111;background:linear-gradient(140deg,#9fc6df,#e3c98f 55%,#d56b6b)}
.spot--room{left:283px;top:308px;width:88px;height:88px;background:linear-gradient(160deg,#e9e4dc,#8b6f58 70%,#5a4a3c)}
.about{position:absolute;left:50px;top:410px;width:168px}
.about h2{font-size:18px;font-weight:700;color:var(--green);margin-bottom:6px}
.about p{font-size:5.2px;line-height:1.35;color:var(--ink-soft);margin-bottom:5px}
.strive{position:absolute;left:227px;top:430px;width:190px}
.strive h3{font-size:11.5px;font-weight:600;color:var(--green);line-height:1.3;margin-bottom:8px}
.strive ul{list-style:none}
.strive li{display:flex;align-items:center;gap:10px;font-size:15.5px;font-weight:600;color:var(--ink);height:26px}
.strive svg{width:14px;height:14px}
.contact-bar{position:absolute;left:0;bottom:0;width:429px;height:46px;background:var(--green);color:var(--white);font-size:8.5px;font-weight:600}
.contact-bar .item{position:absolute;display:flex;align-items:center;gap:6px}
.wa{left:10px;top:7px}
.wa .label{font-size:10px;line-height:1.2}
.wa .label b{font-size:12.5px;display:block}
.ig{left:169px;top:9px}.web{left:169px;top:26px}.mail{left:306px;top:9px}.fb{left:306px;top:26px}
.icon-dot{width:8px;height:8px;border:1.3px solid var(--white);border-radius:50%}
.icon-sq{width:8px;height:8px;background:var(--white);border-radius:1px}

/* BACK */
.banner{position:absolute;left:0;top:0;width:429px;height:70px;background:linear-gradient(100deg,#8a7a3a,#b86a44 35%,#5f8a4a 65%,#9a4a3a)}
.banner-stripe{position:absolute;left:0;top:70px;width:429px;height:12px;background:var(--green)}
.banner h1{position:absolute;left:0;width:100%;top:12px;text-align:center;font-family:'Bebas Neue',sans-serif;font-weight:400;font-size:50px;line-height:1;color:var(--white);text-shadow:0 2px 3px rgba(0,0,0,.5);padding-left:10px}
.section-bar{position:absolute;left:0;width:234px;height:28px;background:var(--green);clip-path:polygon(0 0,100% 0,92% 100%,0 100%);color:var(--white);font-weight:600;font-size:14px;display:flex;align-items:center;padding-left:11px;letter-spacing:.3px}
.section-tail{position:absolute;right:0;width:72px;height:28px;background:var(--green);clip-path:polygon(18% 0,100% 0,100% 100%,0 100%)}
.card{position:absolute;width:95px;height:97px;border:3px solid var(--green);border-radius:6px;overflow:hidden;background:#ccc}
.card .photo{position:absolute;inset:0}
.card .caption{position:absolute;left:4px;right:4px;bottom:4px;min-height:20px;background:var(--caption);color:var(--white);font-size:5.3px;line-height:1.2;text-align:center;display:flex;align-items:center;justify-content:center;padding:2px 3px;border-radius:2px}
.card--space .caption{font-size:8.5px;min-height:16px}
.footer-band{position:absolute;left:0;bottom:0;width:429px;height:22px;background:var(--green)}
</style>
</head>
<body>

<section class="page page--front">
  <div class="hero-photo" role="img" aria-label="Sewing studio with shelves of thread spools and fabric, city view through the window, green tinted"></div>
  <svg class="hero-frame" viewBox="0 0 429 360" aria-hidden="true">
    <path d="M0 290 Q120 265 215 300 Q300 330 429 272 V318 Q300 372 215 344 Q120 312 0 336 Z" fill="#4ba23f"/>
    <path d="M100 0 H330 L312 62 Q306 80 288 80 H142 Q124 80 118 62 Z" fill="#4ba23f"/>
  </svg>
  <div class="brand-tab"><span class="brand-name">MOSS:LOOP HUB</span></div>
  <h1 class="headline"><span class="l1">SUSTAINABILITY</span><span class="l2">FROM HOME</span><span class="l3">JOURNEY STARTS</span></h1>

  <div class="spot spot--hangers" role="img" aria-label="Pastel clothes on hangers"></div>
  <div class="spot spot--hoops" role="img" aria-label="Embroidery hoops and craft supplies"></div>
  <div class="spot spot--room" role="img" aria-label="Creative space interior with work tables"></div>

  <div class="about">
    <h2>ABOUT US</h2>
    <p>MOSS:LOOP HUB is a social enterprise that aims to promote sustainability through enabling and interacting with the community at large by prolonging the life of our preloved apparels.</p>
    <p>Through our products and services that promote green habits such as reusing, repurposing and recreating, we strive to create personal connections and collaborations with you and bind our cause through our interactions in MOSS:LOOP HUB online store or welcome you to our Creative Spaces.</p>
    <p>We hope to bring new energy to the green movement from our Home to yours. Whether it be contributing to our preloved clothing marketplace, to adopting upcycling habits on your own, we believe that a lot can be done to save the Earth, given the right platform and resources.</p>
  </div>

  <div class="strive">
    <h3>OUR STRIVE TOWARD<br>CIRCULAR FASHION</h3>
    <ul>
      <li><svg viewBox="0 0 14 14"><path d="M1 7.5 L5 12 L13 1.5" fill="none" stroke="#3a3a3a" stroke-width="2"/></svg>RE-USE</li>
      <li><svg viewBox="0 0 14 14"><path d="M1 7.5 L5 12 L13 1.5" fill="none" stroke="#3a3a3a" stroke-width="2"/></svg>RE-PURPOSE</li>
      <li><svg viewBox="0 0 14 14"><path d="M1 7.5 L5 12 L13 1.5" fill="none" stroke="#3a3a3a" stroke-width="2"/></svg>RE-CREATE</li>
    </ul>
  </div>

  <footer class="contact-bar">
    <div class="item wa">
      <svg width="14" height="26" viewBox="0 0 14 26"><path d="M3 1 L7 1 L8 7 L5 9 Q5 15 8 18 L11 16 L13 21 L12 25 Q4 25 2 14 Q0 6 3 1 Z" fill="#fff"/></svg>
      <span class="label">WhatsApp :<b>+65 9000 4821</b></span>
    </div>
    <div class="item ig"><span class="icon-dot"></span>@mossloophubsg</div>
    <div class="item web"><span class="icon-dot"></span>www.mossloophub.sg</div>
    <div class="item mail"><svg width="10" height="8" viewBox="0 0 10 8"><rect x=".6" y=".6" width="8.8" height="6.8" fill="none" stroke="#fff" stroke-width="1.1"/><path d="M.6 .8 L5 4.5 L9.4 .8" fill="none" stroke="#fff" stroke-width="1.1"/></svg>askus@mossloophub.sg</div>
    <div class="item fb"><span class="icon-sq"></span>/sgmossloophub</div>
  </footer>
</section>

<section class="page page--back">
  <div class="banner" role="img" aria-label="Colourful fabric bunting photo"></div>
  <h1 class="banner h1" style="background:none">FEATURED PRODUCTS</h1>
  <div class="banner-stripe"></div>

  <div class="section-bar" style="top:98px">CLOTHING</div>
  <div class="section-tail" style="top:98px"></div>
  <div class="card" style="left:10px;top:142px"><div class="photo" role="img" aria-label="Red v-neck t-shirt" style="background:linear-gradient(160deg,#f4f4f4 10%,#d8424a 45%,#b8323a)"></div><div class="caption">Fernway Red V-Neck<br>Cotton Plain T-Shirt</div></div>
  <div class="card" style="left:114px;top:142px"><div class="photo" role="img" aria-label="Black woollen vest" style="background:linear-gradient(160deg,#f1f1f1 10%,#2b2b2b 45%,#1a1a1a)"></div><div class="caption">Black Woollen Blend<br>Vest</div></div>
  <div class="card" style="left:219px;top:142px"><div class="photo" role="img" aria-label="Black knee-length shorts" style="background:linear-gradient(170deg,#eee 5%,#4a4a4c 35%,#3a3a3c)"></div><div class="caption">Quilla Comfortable Black Knee-Length Cotton Trendy Shorts</div></div>
  <div class="card" style="left:323px;top:142px"><div class="photo" role="img" aria-label="Black knee-length shorts" style="background:linear-gradient(170deg,#eee 5%,#46474a 35%,#38393b)"></div><div class="caption">Quilla Comfortable Black Knee-Length Cotton Trendy Shorts</div></div>

  <div class="section-bar" style="top:254px">MERCHANDISE</div>
  <div class="section-tail" style="top:254px"></div>
  <div class="card" style="left:10px;top:299px"><div class="photo" role="img" aria-label="White and blue crocheted necklace" style="background:linear-gradient(150deg,#e9ecec,#8f959a 60%,#5e6468)"></div><div class="caption">White and Blue<br>Crocheted Necklace</div></div>
  <div class="card" style="left:114px;top:299px"><div class="photo" role="img" aria-label="Crocheted stationery holder" style="background:linear-gradient(160deg,#f3f1ec,#c9b48e 50%,#4f8fa8)"></div><div class="caption">Crocheted Stationery<br>Holder</div></div>
  <div class="card" style="left:219px;top:299px"><div class="photo" role="img" aria-label="Blue satin coaster set" style="background:linear-gradient(150deg,#e6e6e6,#2f7f86 45%,#1e4f5e)"></div><div class="caption">Blue Baroque-Style Satin<br>Hand-Stitched Coaster Set</div></div>
  <div class="card" style="left:323px;top:299px"><div class="photo" role="img" aria-label="Brown floral pouch" style="background:linear-gradient(180deg,#d8c08c 40%,#3d5a3e 60%,#7a5a6a)"></div><div class="caption">Brown Floral-Designed<br>Pouch</div></div>

  <div class="section-bar" style="top:412px">CREATIVE SPACES</div>
  <div class="section-tail" style="top:412px"></div>
  <div class="card card--space" style="left:10px;top:455px"><div class="photo" role="img" aria-label="Craft space with embroidery hoops" style="background:linear-gradient(140deg,#9fc6df,#e3c98f 55%,#c96a5a)"></div><div class="caption">Craft Space</div></div>
  <div class="card card--space" style="left:114px;top:455px"><div class="photo" role="img" aria-label="Sewing machine" style="background:linear-gradient(160deg,#ffffff,#dcdde0 55%,#9a9ca2)"></div><div class="caption">Sewing Space</div></div>
  <div class="card card--space" style="left:219px;top:455px"><div class="photo" role="img" aria-label="Photo studio light box with camera" style="background:linear-gradient(160deg,#f4f4f4 10%,#222 45%,#111)"></div><div class="caption">Studio</div></div>

  <div class="footer-band"></div>
</section>

</body>
</html>
```